Harbourline Blinds & Shutters

It Needs to look classy as my target is the upper end of the blind market
I need a Logo design on front and description on back of what i do:
- Roller Blinds
- Vertical Blinds
- Venetian Blinds
- Plantation Shutters
- Aluminum External Shutters
and contact details
Gavin
0418527306
and
Terry
0421690358
Updates
Hi Guys,
Sorry for the no feedback but i was waiting on my logo design. But its done now i have uploaded it. so if you could take a look and send through some designs
Reason: my logo was just finished an i just uploaded it today really dont understand why my deadline has been rached foe my bizcards as it states no deadline. But please extend
Target Market(s)
People that live on the coast and are looking for classy good quality blinds and shutters
Font styles to use
Other font styles liked:
- Copperplate Gothic,open to suggestion
Look and feel
Each slider illustrates characteristics of the customer's brand and the style your logo design should communicate.

```html
<!DOCTYPE html>
<html lang="en">
<head>
<meta charset="utf-8">
<title>Harbourline Blinds &amp; Shutters – Business Card</title>
<link href="https://fonts.googleapis.com/css2?family=Cabin:wght@400;600;700&display=swap" rel="stylesheet">
<style>
  :root {
    --backdrop: #e6e1df;
    --card-cream: #eef3c9;
    --ink-grey: #5a5a5a;
    --band-grey: #6b6b6a;
    --back-grey: #8b8b89;
    --back-pattern: #7b7b79;
    --label-light: #d9dcc0;
  }
  html, body {
    margin: 0;
    width: 1200px;
    height: 800px;
    overflow: hidden;
    background: var(--backdrop);
  }
  .canvas {
    display: block;
    width: 1200px;
    height: 800px;
    font-family: "Cabin", sans-serif;
  }
  .card-front { fill: var(--card-cream); }
  .card-back { fill: var(--back-grey); }
  .contact-band { fill: var(--band-grey); }
  .contact-name { fill: var(--label-light); font-size: 13px; font-weight: 700; letter-spacing: 1.5px; }
  .contact-phone { fill: var(--ink-grey); font-size: 20px; font-weight: 700; letter-spacing: 1px; }
  .service-list { fill: var(--ink-grey); font-size: 16px; font-weight: 600; }
  .brand-mark { fill: var(--ink-grey); }
  .brand-name { fill: var(--ink-grey); font-weight: 600; }
  .back-pattern { fill: var(--back-pattern); }
  .back-panel { fill: var(--card-cream); }
</style>
</head>
<body>
<svg class="canvas" viewBox="0 0 1200 800" xmlns="http://www.w3.org/2000/svg">
  <defs>
    <clipPath id="back-clip"><rect width="540" height="310" rx="6"/></clipPath>
  </defs>

  <!-- Front of card -->
  <g class="front" transform="translate(40,245)">
    <rect class="card-front" width="540" height="310" rx="6"/>

    <g class="brand-lockup">
      <rect class="brand-mark" x="300" y="38" width="14" height="14"/>
      <text class="brand-name" x="322" y="51" font-size="19">HARBOURLINE</text>
      <text class="brand-name" x="323" y="68" font-size="10" letter-spacing="1.2">BLINDS &amp; SHUTTERS</text>
    </g>

    <g transform="rotate(12.5 235 100)">
      <text class="service-list" text-anchor="middle">
        <tspan x="235" y="70">Roller Blinds</tspan>
        <tspan x="235" y="90">Vertical Blinds</tspan>
        <tspan x="235" y="110">Venetian Blinds</tspan>
        <tspan x="235" y="130">Plantation Shutters</tspan>
        <tspan x="235" y="150">Aluminum External Shutters</tspan>
      </text>
    </g>

    <polygon class="contact-band" points="0,118 540,238 540,260 0,140"/>

    <text class="contact-name" x="14" y="135" transform="rotate(12.5 14 135)">TERRY</text>
    <text class="contact-phone" x="10" y="163" transform="rotate(12.5 10 163)">042 169 0358</text>

    <text class="contact-name" x="526" y="252" text-anchor="end" transform="rotate(12.5 526 252)">GAVIN</text>
    <text class="contact-phone" x="490" y="219" text-anchor="end" transform="rotate(12.5 490 219)">041 852 7306</text>
  </g>

  <!-- Back of card -->
  <g class="back" transform="translate(620,245)">
    <g clip-path="url(#back-clip)">
      <rect class="card-back" width="540" height="310"/>
      <rect class="back-pattern" x="50" y="0" width="440" height="95" role="img" aria-label="Large faded blind slats motif"/>
      <polygon class="back-panel" points="0,120 540,260 540,340 0,200"/>
      <g transform="rotate(14.5 270 225)">
        <text class="brand-name" x="270" y="222" font-size="30" text-anchor="middle" letter-spacing="1">HARBOURLINE</text>
        <text class="brand-name" x="270" y="242" font-size="13" text-anchor="middle" letter-spacing="2">BLINDS &amp; SHUTTERS</text>
      </g>
    </g>
  </g>
</svg>
</body>
</html>
```